Clothing for elderly and disabled persons business card

I have seen a design on the Prism website with a partial hand holding a heart I would like that to be incorporated above the i in Willowmere
The colours should be either soft green and pinks.
The final design should communicate care, love, easy fit comfort clothing for the frail and disabled.

Willowmere
Gentle WearClothing

Target Market(s)

Nursing Homes, Elderly in care or just anyone with limited mobility

Industry/Entity Type

Clothing

Contact Information for Business Card

Willowmere Gentle Wear Clothing
Carol Hensley Owner Sales Consultant
Phone 0451 726 083 Fax 08 9627 4418
Email: willowmeregentlewear@examplemail.com

Requirements
Nice to have
• A hand holding a heart this must form part of the i in Willowmere, instead of the dot above the i I want the hand holding the heart.

```html
<!DOCTYPE html>
<html lang="en">
<head>
<meta charset="utf-8">
<title>Willowmere Gentle Wear Clothing – Business Cards</title>
<link rel="stylesheet" href="https://fonts.googleapis.com/css2?family=EB+Garamond:wght@400&family=Lato:wght@400;700&display=swap">
<style>
  :root {
    --sheet-grey: #d9d9d9;
    --label-ink: #1a1a1a;
    --card-white: #ffffff;
    --brand-green: #068c3a;
    --brand-purple: #6a2a8a;
    --lavender-soft: #ddd1ea;
    --sage-soft: #e6ede3;
    --text-grey: #8a8a8a;
    --name-grey: #9a9a9a;
    --crop-grey: #b5b5b5;
    --back-tint: rgba(255, 255, 255, 0.2);
  }
  * { box-sizing: border-box; margin: 0; padding: 0; }
  html, body { width: 1200px; height: 899px; overflow: hidden; }
  body {
    background: var(--sheet-grey);
    position: relative;
    font-family: "Lato", Arial, sans-serif;
  }
  .side-label {
    position: absolute;
    top: 112px;
    width: 537px;
    text-align: center;
    font-size: 22px;
    color: var(--label-ink);
    letter-spacing: 0.5px;
  }
  .side-label--front { left: 51px; }
  .side-label--back { left: 617px; }

  .card {
    position: absolute;
    width: 537px;
    height: 309px;
    overflow: hidden;
  }
  .card--front { background: var(--card-white); left: 51px; }
  .card--back { background: var(--brand-green); left: 617px; }
  .card--row1 { top: 169px; }
  .card--row2 { top: 502px; }

  .crop-mark {
    position: absolute;
    width: 16px;
    height: 16px;
    border: 0 solid var(--crop-grey);
  }
  .crop-mark--bl { left: 0; bottom: 0; border-top-width: 1px; border-right-width: 1px; }
  .crop-mark--tr { right: 0; top: 0; border-bottom-width: 1px; border-left-width: 1px; }
  .card--back .crop-mark { border-color: rgba(255,255,255,0.7); }

  .soft-wash {
    position: absolute;
    left: 112px;
    top: 22px;
    width: 170px;
    height: 160px;
    border-radius: 50%;
  }
  .card--front .soft-wash {
    background: radial-gradient(circle at 50% 40%, var(--lavender-soft) 0%, var(--lavender-soft) 45%, var(--sage-soft) 80%, rgba(230,237,227,0) 100%);
  }
  .card--back .soft-wash {
    background: radial-gradient(circle at 50% 40%, var(--back-tint) 0%, rgba(255,255,255,0.12) 55%, rgba(255,255,255,0) 100%);
  }

  .brand {
    position: absolute;
    display: flex;
    align-items: center;
    gap: 8px;
  }
  .brand__dot {
    width: 16px;
    height: 16px;
    border-radius: 50%;
    flex: none;
  }
  .brand__name {
    font-family: "EB Garamond", Georgia, serif;
    font-size: 29px;
    font-weight: 400;
    white-space: nowrap;
    line-height: 1;
  }
  .card--front .brand { left: 52px; top: 80px; }
  .card--front .brand__dot { background: var(--brand-purple); }
  .card--front .brand__name { color: var(--brand-green); }
  .card--back .brand { left: 46px; top: 138px; }
  .card--back .brand__dot { background: var(--card-white); }
  .card--back .brand__name { color: var(--card-white); }

  .contact-person {
    position: absolute;
    left: 306px;
    top: 128px;
    color: var(--text-grey);
  }
  .contact-person__name {
    font-size: 19px;
    font-weight: 700;
    color: var(--name-grey);
    line-height: 1.1;
  }
  .contact-person__role {
    font-size: 10px;
    line-height: 1.3;
    margin-bottom: 4px;
  }
  .contact-person__line {
    font-size: 15px;
    line-height: 1.4;
  }
  .contact-web {
    position: absolute;
    left: 90px;
    top: 230px;
    font-size: 14px;
    line-height: 1.5;
    color: var(--text-grey);
  }
</style>
</head>
<body>
  <div class="side-label side-label--front">FRONT</div>
  <div class="side-label side-label--back">BACK</div>

  <section class="card card--front card--row1">
    <div class="soft-wash" role="img" aria-label="Soft lavender and sage background wash"></div>
    <div class="brand"><span class="brand__dot"></span><span class="brand__name">Willowmere Gentle Wear Clothing</span></div>
    <div class="contact-person">
      <p class="contact-person__name">Renee Marlowe</p>
      <p class="contact-person__role">Owner/Sales Consultant</p>
      <p class="contact-person__line">Phone 0422 815 307</p>
      <p class="contact-person__line">Fax 08 9627 4418</p>
    </div>
    <div class="contact-web">
      <p>Email sales@willowmeregentlewear.com</p>
      <p>Website www.willowmeregentlewear.com</p>
    </div>
    <span class="crop-mark crop-mark--bl"></span>
    <span class="crop-mark crop-mark--tr"></span>
  </section>

  <section class="card card--back card--row1">
    <div class="soft-wash" role="img" aria-label="Soft pale green background wash"></div>
    <div class="brand"><span class="brand__dot"></span><span class="brand__name">Willowmere Gentle Wear Clothing</span></div>
    <span class="crop-mark crop-mark--bl"></span>
    <span class="crop-mark crop-mark--tr"></span>
  </section>

  <section class="card card--front card--row2">
    <div class="soft-wash" role="img" aria-label="Soft lavender and sage background wash"></div>
    <div class="brand"><span class="brand__dot"></span><span class="brand__name">Willowmere Gentle Wear Clothing</span></div>
    <div class="contact-person">
      <p class="contact-person__name">Carol Hensley</p>
      <p class="contact-person__role">Owner/Sales Consultant</p>
      <p class="contact-person__line">Phone 0451 726 083</p>
      <p class="contact-person__line">Fax 08 9627 4418</p>
    </div>
    <div class="contact-web">
      <p>Email sales@willowmeregentlewear.com</p>
      <p>Website www.willowmeregentlewear.com</p>
    </div>
    <span class="crop-mark crop-mark--bl"></span>
    <span class="crop-mark crop-mark--tr"></span>
  </section>

  <section class="card card--back card--row2">
    <div class="soft-wash" role="img" aria-label="Soft pale green background wash"></div>
    <div class="brand"><span class="brand__dot"></span><span class="brand__name">Willowmere Gentle Wear Clothing</span></div>
    <span class="crop-mark crop-mark--bl"></span>
    <span class="crop-mark crop-mark--tr"></span>
  </section>
</body>
</html>
```